Quillmere Financial Plans

I am looking for a complete resdesign of my small financial presentation. This is a Word Doc/PDF that I print off when meeting with people in private. I often present my "two pager" that I have been using for years and years. It tells them the basics of what I do, how I help people and foundational financial principles.

I have recently gone out on my own in business and have completely rebranded. This presentation is my most used tool, so it is the first of many things I would like to redo. I am hoping it will somehow coordinate with the colors of my business, not necessarily the EXACT same 3 colors everywhere, but have the design colors compliment.

I've uploaded all my logo designs, as well as the current "two-pager". I am not against it going to 3 pages if needed. As it will still land on 2 pages with duplex printing.

It has always been VERY simple. I am wanting it built into a more professional and design specific format, to show off my branding, without being over cluttered.

I am completely open to ANY graphics changes. Obviously some are very novice, the house on the last page has always been overly simplified.

```html
<!DOCTYPE html>
<html lang="en">
<head>
<meta charset="utf-8">
<title>Quillmere Financial Plans – The Financial Challenge</title>
<link href="https://fonts.googleapis.com/css2?family=Montserrat:wght@400;500;600;700;800&display=swap" rel="stylesheet">
<style>
:root{
  --navy:#18213a;
  --green:#21a63f;
  --green-dark:#17852f;
  --grey:#6e7075;
  --grey-light:#9a9ca0;
  --teal:#0f2a33;
  --red:#e3262b;
  --white:#ffffff;
  --sky:#cfe4f4;
  --stage:#3a3a3a;
}
*{box-sizing:border-box;margin:0;padding:0}
html,body{width:723px;height:1200px;overflow:hidden}
body{background:var(--stage);font-family:"Montserrat",sans-serif;color:var(--navy)}
.sheet-frame{position:absolute;left:151px;width:420px;height:590px;overflow:hidden;box-shadow:0 3px 10px rgba(0,0,0,.45)}
.sheet-frame.front{top:7px}
.sheet-frame.back{top:603px}
.sheet{position:absolute;left:0;top:0;width:605px;height:850px;transform:scale(.6942);transform-origin:0 0;background:var(--white);overflow:hidden}
.abs{position:absolute}

/* front page */
.brand{left:40px;top:36px;width:235px;text-align:center}
.brand-name{font-size:37px;font-weight:600;letter-spacing:-.5px;color:var(--navy);line-height:1}
.brand-tag{display:flex;align-items:center;gap:8px;font-size:12px;font-weight:600;letter-spacing:3px;margin-top:4px;justify-content:center}
.brand-tag::before,.brand-tag::after{content:"";width:30px;height:2px;background:currentColor}
.title-band{left:0;top:106px;width:605px;height:122px;background:var(--navy)}
.title{left:43px;top:124px;font-size:27px;font-weight:800;line-height:.98;color:var(--white)}
.title .accent{color:var(--green)}
.hero-photo{left:345px;top:22px;width:220px;height:220px;border-radius:50%;background:radial-gradient(circle at 40% 40%,#e4e9ee 0%,#b9c4cf 70%,#9aa6b2 100%);border:6px solid var(--white)}
.challenge{left:0;top:228px;width:605px;height:315px;background:var(--green)}
.badge{left:56px;width:82px;height:82px;border-radius:50%;background:var(--white);border:4px solid var(--navy);display:flex;flex-direction:column;align-items:center;justify-content:center;font-weight:800;font-size:9.5px;color:var(--navy)}
.badge svg{margin-bottom:3px}
.stats{left:160px;top:256px;width:395px;color:var(--white);font-size:7.6px;font-weight:600;line-height:1.3;text-transform:uppercase}
.stats p{margin-bottom:9px}
.stats .src{color:var(--navy)}
.stats hr{border:0;border-top:1px dashed rgba(255,255,255,.6);margin:6px 0 8px}
.tab{background:var(--green);color:var(--white);font-weight:700;text-align:center;clip-path:polygon(0 0,100% 0,93% 100%,7% 100%)}
.who-tab{left:168px;top:543px;width:270px;height:25px;font-size:11px;line-height:25px}
.services{left:30px;top:585px;width:545px;display:flex}
.service{flex:1;text-align:center;border-right:1px solid #c6cbd4;height:132px;font-size:7px;font-weight:700;text-transform:uppercase}
.service:last-child{border-right:0}
.service .icon{height:48px;display:flex;align-items:center;justify-content:center}
.service .name{margin-top:8px;color:var(--navy)}
.service .sub{color:var(--green);margin-top:12px;line-height:1.25}
.how-line{left:0;top:724px;width:605px;height:3px;background:var(--navy)}
.how-tab{left:190px;top:724px;width:230px;height:26px;background:var(--navy);color:var(--white);font-size:12px;font-weight:700;text-align:center;line-height:25px;clip-path:polygon(0 0,100% 0,93% 100%,7% 100%)}
.savings-label{left:136px;top:776px;font-size:8.5px;font-weight:600}
.goals{top:770px;font-size:8.5px;font-weight:600;text-transform:uppercase;line-height:22px}
.goals li{list-style:none;display:flex;align-items:center;gap:9px}
.goals li::before{content:"";width:11px;height:11px;border:1.6px solid var(--green)}
.partners{left:42px;top:828px;width:530px;height:14px;background:var(--sky);display:flex;justify-content:space-around;align-items:center}
.partners span{width:30px;height:6px;border-radius:3px;background:#8fb4d2}

/* back page */
.rule-band{left:0;top:0;width:605px;height:355px;background:var(--navy)}
.rule-title{left:0;top:28px;width:605px;text-align:center;color:var(--white);font-size:19px;font-weight:700}
.rule-cols{left:42px;top:67px;display:flex;gap:4px}
.rule-col{width:130px}
.rule-head,.rule-row{display:flex;justify-content:space-between;padding:0 8px;font-size:7.5px;font-weight:600}
.rule-head{background:var(--green);color:var(--white);height:22px;line-height:22px;font-size:8.5px;margin-bottom:4px}
.rule-row{background:var(--grey);color:var(--white);height:22px;line-height:22px;margin-bottom:4px}
.doubles{left:42px;top:292px;display:flex;gap:4px}
.doubles div{width:130px;height:36px;background:var(--green);color:var(--white);font-size:8px;font-weight:700;text-align:center;display:flex;align-items:center;justify-content:center;line-height:1.1}
.roof{left:42px;top:373px}
.roof-label{left:0;top:430px;width:605px;text-align:center;color:var(--white);font-weight:800;font-size:18px;letter-spacing:.5px}
.pillars{left:42px;top:482px;display:flex;gap:5px}
.pillar{width:128px;height:205px;color:var(--white);text-align:center;padding-top:14px;position:relative;font-size:10px;font-weight:600;line-height:1.3}
.pillar.g{background:var(--green)}
.pillar.n{background:var(--navy)}
.pillar h3{font-size:14px;font-weight:700;margin-bottom:20px}
.pillar .tagbox{position:absolute;left:26px;bottom:14px;width:76px;height:15px;background:var(--red);font-weight:800;font-size:10px;line-height:15px}
.foundation{left:42px;top:693px;width:526px;height:42px;background:var(--navy);border:3px solid var(--grey);display:flex;justify-content:space-around;align-items:center;color:var(--white);font-size:9.5px;font-weight:600;text-align:center;line-height:1.3}
.footer-band{left:0;top:758px;width:605px;height:92px;background:var(--teal)}
.footer-brand{left:185px;top:785px;width:235px;text-align:center;color:var(--white)}
</style>
</head>
<body>

<div class="sheet-frame front">
<section class="sheet">
  <div class="abs brand">
    <div class="brand-name">QUILLMERE</div>
    <div class="brand-tag">FINANCIAL PLANS</div>
  </div>
  <div class="abs title-band"></div>
  <h1 class="abs title">THE<br><span class="accent">FINANCIAL</span><br>CHALLENGE</h1>
  <div class="abs hero-photo" role="img" aria-label="Photo of hands reviewing financial charts on a clipboard"></div>
  <div class="abs challenge"></div>
  <div class="abs badge" style="top:250px">
    <svg width="22" height="22" viewBox="0 0 22 22"><circle cx="11" cy="11" r="9" fill="#e8b33a" stroke="var(--navy)" stroke-width="1.5"/><text x="11" y="15" font-size="11" text-anchor="middle" font-weight="700" fill="var(--navy)">$</text></svg>SAVINGS</div>
  <div class="abs badge" style="top:343px">
    <svg width="22" height="22" viewBox="0 0 22 22"><circle cx="11" cy="11" r="9" fill="#e8b33a" stroke="var(--navy)" stroke-width="1.5"/><text x="11" y="15" font-size="10" text-anchor="middle" font-weight="700" fill="var(--navy)">%</text></svg>DEBT</div>
  <div class="abs badge" style="top:438px">
    <svg width="22" height="22" viewBox="0 0 22 22"><rect x="4" y="5" width="14" height="12" rx="2" fill="#e8b33a" stroke="var(--navy)" stroke-width="1.5"/></svg>INSURANCE</div>
  <div class="abs stats">
    <p>49% of Canadian employees are living paycheque to paycheque. 25% of Canadians are unable to cover an unexpected $500 expense<br><span class="src">- National Stats Bureau (Feb 2023)</span></p>
    <p>49% of Canadian employees are living paycheque to paycheque. 25% of Canadians are unable to cover an unexpected $500 expense<br><span class="src">- National Stats Bureau (Feb 2023)</span></p>
    <hr>
    <p>The average Canadian has $22,131 in consumer debt. Which excludes mortgages.<br><span class="src">- Creditline Data (Aug 2024)</span></p>
    <p>Over 55% of Canadians hold credit card debt and the total Canadian household debt has increased to $2.52trillion, including consumer credit, mortgage and non-mortgage loans.<br><span class="src">- Bankers Forum (Aug 2024)</span></p>
    <hr>
    <p>45% of Canadians do not have individual life insurance coverage, but 48% say their families would face financial trouble within 6 months of losing someone.<br><span class="src">- Insurance Research Intl. (Apr 2023)</span></p>
    <p>2-in-5 Canadians (43% women / 44% men) will be diagosed with a form of cancer or other critical illness during their lifetime. Every 7 seconds.<br><span class="src">- Health Data Hub (June 2024)</span></p>
  </div>

  <div class="abs tab who-tab">WHO ARE WE AND WHAT DO WE DO?</div>
  <div class="abs services">
    <div class="service"><div class="icon"><svg width="44" height="34" viewBox="0 0 44 34"><rect x="3" y="9" width="38" height="20" rx="2" fill="var(--navy)"/><rect x="7" y="13" width="30" height="12" fill="#3d7fd1"/><circle cx="22" cy="19" r="4" fill="var(--white)"/><rect x="6" y="4" width="30" height="4" fill="#3d7fd1"/></svg></div><div class="name">Cash Flow</div><div class="sub">Analyze</div><div class="sub">Free Up</div></div>
    <div class="service"><div class="icon"><svg width="44" height="44" viewBox="0 0 44 44"><path d="M4 22 A18 18 0 0 1 40 22 Z" fill="#2f6fc7"/><path d="M22 22 V36 a3 3 0 0 1 -6 0" fill="none" stroke="var(--navy)" stroke-width="2"/></svg></div><div class="name">Cash Flow Protection</div><div class="sub">Income Protection</div><div class="sub">Life Insurance &nbsp; CI/DI Insurance</div></div>
    <div class="service"><div class="icon"><svg width="44" height="34" viewBox="0 0 44 34"><rect x="3" y="5" width="38" height="25" rx="3" fill="none" stroke="var(--navy)" stroke-width="2.5"/><rect x="3" y="11" width="38" height="5" fill="#3d7fd1"/><line x1="8" y1="32" x2="36" y2="2" stroke="var(--navy)" stroke-width="2.5"/></svg></div><div class="name">Debt Management</div><div class="sub">20%<br>↓<br>6%-7%</div></div>
    <div class="service"><div class="icon"><svg width="48" height="34" viewBox="0 0 48 34"><rect x="4" y="8" width="30" height="20" rx="2" fill="#3d7fd1" stroke="var(--navy)" stroke-width="2"/><path d="M34 14 h7 l4 6 v8 h-11z" fill="#3d7fd1" stroke="var(--navy)" stroke-width="2"/><circle cx="12" cy="29" r="3.5" fill="var(--navy)"/><circle cx="38" cy="29" r="3.5" fill="var(--navy)"/><path d="M19 12 v10 M14 17 h10" stroke="var(--white)" stroke-width="3"/></svg></div><div class="name">Emergency Fund</div><div class="sub">If/When</div><div class="sub">3/6<br>Months</div></div>
    <div class="service"><div class="icon"><svg width="44" height="34" viewBox="0 0 44 34"><ellipse cx="22" cy="19" rx="16" ry="12" fill="#2f6fc7"/><rect x="11" y="27" width="5" height="6" fill="#2f6fc7"/><rect x="27" y="27" width="5" height="6" fill="#2f6fc7"/><rect x="19" y="7" width="7" height="2" fill="var(--navy)"/></svg></div><div class="name">Build Wealth</div><div class="sub">Financial Independence Number (F.I.N)</div></div>
    <div class="service"><div class="icon"><svg width="40" height="44" viewBox="0 0 40 44"><rect x="4" y="3" width="32" height="36" rx="2" fill="#3d7fd1" stroke="var(--navy)" stroke-width="2.5"/><rect x="9" y="8" width="22" height="26" fill="none" stroke="var(--navy)" stroke-width="2"/><circle cx="20" cy="21" r="5" fill="none" stroke="var(--navy)" stroke-width="2"/></svg></div><div class="name">Preserve</div><div class="sub">Leaving a Legacy</div><div class="sub">Will Prep</div></div>
  </div>

  <div class="abs how-line"></div>
  <div class="abs how-tab">HOW ARE WE DOING IT?</div>
  <svg class="abs" style="left:42px;top:745px" width="86" height="86" viewBox="0 0 86 86">
    <circle cx="43" cy="43" r="41" fill="var(--grey-light)"/>
    <path d="M43 43 L43 2 A41 41 0 0 0 43 84 Z" fill="var(--navy)"/>
    <path d="M43 43 L43 2 A41 41 0 0 1 84 43 Z" fill="var(--green)"/>
    <path d="M43 43 L84 43 A41 41 0 0 1 72 72 Z" fill="#b3151b"/>
    <text x="22" y="44" font-size="6" fill="var(--white)" text-anchor="middle" font-weight="600">Living</text>
    <text x="22" y="51" font-size="6" fill="var(--white)" text-anchor="middle" font-weight="600">Expenses</text>
    <text x="62" y="26" font-size="6" fill="var(--navy)" text-anchor="middle" font-weight="600">Taxes</text>
    <text x="54" y="74" font-size="6" fill="var(--navy)" text-anchor="middle" font-weight="600">Debt</text>
  </svg>
  <div class="abs savings-label">Savings ⟶</div>
  <ul class="abs goals" style="left:255px"><li>Retirement Savings</li><li>Children's Education</li></ul>
  <ul class="abs goals" style="left:432px"><li>Proper Protection</li><li>Fredom From Debt</li></ul>
  <div class="abs partners" aria-label="Partner insurers"><span></span><span></span><span></span><span></span><span></span><span></span><span></span><span></span><span></span><span></span></div>
</section>
</div>

<div class="sheet-frame back">
<section class="sheet">
  <div class="abs rule-band"></div>
  <h2 class="abs rule-title">RULE OF 72</h2>
  <div class="abs rule-cols">
    <div class="rule-col"><div class="rule-head"><span>AGE</span><span>4%</span></div>
      <div class="rule-row"><span>29</span><span>$10,000</span></div><div class="rule-row"><span>47</span><span>$20,000</span></div><div class="rule-row"><span>65</span><span>$40,000</span></div></div>
    <div class="rule-col"><div class="rule-head"><span>AGE</span><span>6%</span></div>
      <div class="rule-row"><span>29</span><span>$10,000</span></div><div class="rule-row"><span>41</span><span>$20,000</span></div><div class="rule-row"><span>53</span><span>$40,000</span></div><div class="rule-row"><span>65</span><span>$80,000</span></div></div>
    <div class="rule-col"><div class="rule-head"><span>AGE</span><span>8%</span></div>
      <div class="rule-row"><span>29</span><span>$10,000</span></div><div class="rule-row"><span>38</span><span>$20,000</span></div><div class="rule-row"><span>47</span><span>$40,000</span></div><div class="rule-row"><span>56</span><span>$80,000</span></div><div class="rule-row"><span>56</span><span>$160,000</span></div></div>
    <div class="rule-col"><div class="rule-head"><span>AGE</span><span>12%</span></div>
      <div class="rule-row"><span>29</span><span>$10,000</span></div><div class="rule-row"><span>35</span><span>$20,000</span></div><div class="rule-row"><span>41</span><span>$40,000</span></div><div class="rule-row"><span>47</span><span>$80,000</span></div><div class="rule-row"><span>53</span><span>$160,000</span></div><div class="rule-row"><span>59</span><span>$320,000</span></div><div class="rule-row"><span>59</span><span>$640,000</span></div></div>
  </div>
  <div class="abs doubles"><div>MONEY DOUBLES<br>EVERY 18 YEARS</div><div>MONEY DOUBLES<br>EVERY 12 YEARS</div><div>MONEY DOUBLES<br>EVERY 9 YEARS</div><div>MONEY DOUBLES<br>EVERY 6 YEARS</div></div>

  <svg class="abs roof" width="526" height="104" viewBox="0 0 526 104">
    <polygon points="263,2 524,100 2,100" fill="var(--green)" stroke="var(--navy)" stroke-width="3"/>
    <line x1="2" y1="102" x2="524" y2="102" stroke="var(--navy)" stroke-width="3"/>
  </svg>
  <div class="abs roof-label">STRUCTURE</div>
  <div class="abs pillars">
    <div class="pillar g"><h3>HOME</h3>Partner with<br>mortgage<br>brokers for best<br>rates<br><br>Mortgage<br>insurance alter-<br>natives<div class="tagbox">SELL</div></div>
    <div class="pillar n"><h3>RRSP</h3><br>Tax<br>Deduction<br><br><br>Tax<br>Deverred<div class="tagbox">100$</div></div>
    <div class="pillar g"><h3>TFSA</h3>No Tax Deductions<br>Tax Free Growth<br>2009-$95,000<br>Limit 2023-<br>47,000/YR<div class="tagbox">0% TAX</div></div>
    <div class="pillar n"><h3>PERM LIFE</h3><br>No Tax Deduction<br>Qualify<br>Tax Deferred<br>Growth<div class="tagbox">0% TAX</div></div>
  </div>
  <div class="abs foundation"><span>LIFE INSURANCE ILLNESS<br>CRITICAL/DISABILITY</span><span>DEBT MANAGEMENT<br>CASH FLOW</span></div>
  <div class="abs footer-band"></div>
  <div class="abs footer-brand">
    <div class="brand-name" style="color:var(--white)">QUILLMERE</div>
    <div class="brand-tag">FINANCIAL PLANS</div>
  </div>
</section>
</div>

</body>
</html>
```